Zielgruppe
Wir sind eine Wäscherei.
Zielgruppe: Kunden aus der Hotel- und Gastronomiebranche
Aufgabenstellung
Wir benötigen einen 2-seitigen Flyer DIN lang. 9,8 x21cm
TextInhalte sind in der Vorlage-Datei.
Bilder sind eingefügt.

```html
<!DOCTYPE html>
<html lang="de">
<head>
<meta charset="utf-8">
<title>Flyer Serviettenfaltservice – Wäscherei Lindenfeld</title>
<link rel="stylesheet" href="https://fonts.googleapis.com/css2?family=Open+Sans:wght@300;400;600;700&display=swap">
<style>
  :root {
    --pink: #e5168c;
    --grey-dark: #5a5a5c;
    --grey-text: #4a4a4c;
    --grey-small: #6a6a6c;
    --white: #ffffff;
    --page: #ecebe8;
  }
  html, body {
    margin: 0;
    width: 1200px;
    height: 1200px;
    overflow: hidden;
    background: var(--page);
    font-family: "Open Sans", Arial, sans-serif;
  }
  .flyer-side {
    position: absolute;
    left: 20px;
    width: 1160px;
    height: 547px;
    display: block;
  }
  .flyer-side--front { top: 40px; }
  .flyer-side--back { top: 613px; }
  .flyer-side text { font-family: "Open Sans", Arial, sans-serif; }
  .headline-light { font-weight: 300; fill: var(--white); }
  .headline { font-weight: 400; fill: var(--white); letter-spacing: 4px; }
  .brand-name { font-weight: 700; fill: var(--pink); }
  .contact { font-weight: 400; fill: var(--grey-text); }
  .body-copy { font-weight: 400; fill: var(--grey-text); }
  .body-copy .strong { font-weight: 700; }
  .small-print { font-weight: 400; fill: var(--grey-small); }
  .price-title { font-weight: 700; fill: var(--white); }
  .price-value { font-weight: 400; fill: var(--white); }
  .price-value .amount { font-weight: 700; }
  .price-unit { font-weight: 400; fill: var(--white); }
  .badge-neu { font-weight: 400; fill: var(--pink); }
  .badge-sub { font-weight: 600; fill: var(--grey-dark); }
  .service-item { font-weight: 600; fill: var(--grey-text); }
  .tick { fill: none; stroke: var(--pink); stroke-width: 5; stroke-linecap: round; stroke-linejoin: round; }
</style>
</head>
<body>

<!-- Vorderseite -->
<svg class="flyer-side flyer-side--front" viewBox="0 0 1886 890" preserveAspectRatio="none" xmlns="http://www.w3.org/2000/svg">
  <defs>
    <radialGradient id="bgFront" cx="60%" cy="50%" r="70%">
      <stop offset="0" stop-color="#fbfbfb"/>
      <stop offset="1" stop-color="#cfcfd0"/>
    </radialGradient>
    <linearGradient id="tableScene" x1="0" y1="0" x2="1" y2="1">
      <stop offset="0" stop-color="#e9e9ea"/>
      <stop offset="0.6" stop-color="#f6f6f6"/>
      <stop offset="1" stop-color="#b9b9bb"/>
    </linearGradient>
  </defs>

  <rect class="card-bg" width="1886" height="890" fill="url(#bgFront)"/>
  <rect class="header-strip" x="640" width="1246" height="156" fill="var(--white)"/>

  <!-- Titelbänder -->
  <rect class="title-band" x="780" y="156" width="1106" height="106" fill="var(--pink)"/>
  <rect class="title-band" x="830" y="272" width="1056" height="106" fill="var(--pink)"/>

  <!-- Bogenkanten -->
  <path class="arc-grey" d="M0 270 H850 C875 420 860 560 800 700 C760 790 720 850 690 890 H0Z" fill="var(--grey-dark)"/>
  <path class="arc-pink" d="M0 0 H625 C790 170 850 330 832 480 C815 640 740 790 665 890 H0Z" fill="var(--pink)"/>
  <path class="photo-area" role="img" aria-label="Foto: gedeckter Tisch mit weißer Tischdecke, gefalteter Stoffserviette, Weingläsern und Besteck"
        d="M0 0 H600 C760 170 825 330 808 480 C792 640 718 790 642 890 H0Z" fill="url(#tableScene)"/>

  <!-- Kopfzeile -->
  <text class="brand-name" x="1075" y="95" font-size="40">Wäscherei Lindenfeld</text>
  <text class="contact" font-size="20">
    <tspan x="1525" y="62">Ahornweg 12 – 70999 Musterstadt</tspan>
    <tspan x="1525" y="90">Tel. +49 (0) 7000 / 12 34 56</tspan>
    <tspan x="1525" y="118">E-Mail. info@lindenfeld.de</tspan>
  </text>

  <!-- Titel -->
  <text class="headline-light" x="822" y="236" font-size="62" letter-spacing="3">IHR</text>
  <text class="headline" x="948" y="240" font-size="92">SERVIETTEN-</text>
  <text class="headline" x="896" y="364" font-size="92">FALTSERVICE</text>

  <!-- Neu-Kennzeichnung -->
  <circle class="badge" cx="1734" cy="320" r="124" fill="var(--white)" stroke="var(--pink)" stroke-width="4"/>
  <text class="badge-neu" x="1734" y="335" font-size="92" text-anchor="middle">NEU</text>
  <text class="badge-sub" x="1742" y="364" font-size="28" text-anchor="middle">ab November</text>

  <!-- Fließtext -->
  <text class="body-copy" font-size="26">
    <tspan x="890" y="488">Wir <tspan class="strong">optimieren</tspan> Ihren Serviettenfaltprozess.</tspan>
    <tspan x="890" y="526">Wir <tspan class="strong">entlasten</tspan> Sie von dieser demotivierenden und unproduktiven Tätigkeit.</tspan>
    <tspan x="890" y="564">Wir falten Ihnen Ihre Stoffservietten oder unsere Mietservietten vor.</tspan>
    <tspan x="890" y="640"><tspan class="strong">Hygienisch, zuverlässig und wirtschaftlich</tspan> – bereit für die Mise en Place.</tspan>
  </text>

  <text class="small-print" font-size="18.5">
    <tspan x="805" y="741">Weitere Formen sind auf Anfrage möglich.</tspan>
    <tspan x="805" y="767">Bei Bedarf stellen wir Ihnen</tspan>
    <tspan x="805" y="793">Mietservietten für nur 0,25 €*</tspan>
    <tspan x="805" y="819">je Stück zur Verfügung.</tspan>
    <tspan x="805" y="875">Mindestabnahmemenge: 100 Stück</tspan>
  </text>

  <!-- Preisfelder -->
  <path class="price-box price-box--pink" d="M1193 890 V748 Q1193 720 1221 720 H1449 Q1477 720 1477 748 V890Z" fill="var(--pink)"/>
  <text class="price-title" x="1326" y="782" font-size="23" text-anchor="middle">Welle, Kerze, Fächer</text>
  <text class="price-value" x="1208" y="835" font-size="34">nur <tspan class="amount" font-size="46">0,20 €</tspan> <tspan font-size="34">*</tspan></text>
  <text class="price-unit" x="1435" y="858" font-size="18" text-anchor="end">je Faltung</text>

  <path class="price-box price-box--grey" d="M1497 890 V748 Q1497 720 1525 720 H1802 Q1830 720 1830 748 V890Z" fill="var(--grey-dark)"/>
  <text class="price-title" x="1663" y="782" font-size="23" text-anchor="middle">Pyramide, Bischofsmütze</text>
  <text class="price-value" x="1518" y="835" font-size="34">nur <tspan class="amount" font-size="46">0,35 €</tspan> <tspan font-size="34">*</tspan></text>
  <text class="price-unit" x="1798" y="858" font-size="18" text-anchor="end">je Faltung</text>

  <text class="small-print" font-size="18" transform="translate(1862 880) rotate(-90)">*zzgl. 19 % MwSt.</text>
</svg>

<!-- Rückseite -->
<svg class="flyer-side flyer-side--back" viewBox="0 0 1886 890" preserveAspectRatio="none" xmlns="http://www.w3.org/2000/svg">
  <defs>
    <radialGradient id="bgBack" cx="35%" cy="50%" r="70%">
      <stop offset="0" stop-color="#fbfbfb"/>
      <stop offset="1" stop-color="#d2d2d3"/>
    </radialGradient>
    <linearGradient id="teamScene" x1="0" y1="0" x2="0" y2="1">
      <stop offset="0" stop-color="#6f6a63"/>
      <stop offset="0.45" stop-color="#4a4844"/>
      <stop offset="0.75" stop-color="#b8b4ae"/>
      <stop offset="1" stop-color="#8d8b87"/>
    </linearGradient>
  </defs>

  <rect class="card-bg" width="1886" height="890" fill="url(#bgBack)"/>

  <!-- Titelbänder -->
  <rect class="title-band" x="0" y="128" width="1140" height="102" fill="var(--pink)"/>
  <rect class="title-band" x="0" y="243" width="1100" height="104" fill="var(--pink)"/>

  <!-- Bogenkanten -->
  <path class="arc-pink" d="M1886 0 H1220 C1110 130 1080 300 1085 420 C1090 560 1150 740 1270 890 H1886Z" fill="var(--pink)"/>
  <path class="arc-grey" d="M1886 300 H1120 C1085 420 1080 560 1110 660 C1150 780 1210 850 1260 890 H1886Z" fill="var(--grey-dark)"/>
  <path class="photo-area" role="img" aria-label="Foto: Team der Wäscherei in weißen Kitteln vor der geöffneten Halle"
        d="M1886 0 H1266 C1160 140 1120 320 1118 440 C1116 600 1170 770 1290 890 H1886Z" fill="url(#teamScene)"/>

  <!-- Titel -->
  <text class="headline-light" x="50" y="202" font-size="62" letter-spacing="3">IHRE</text>
  <text class="headline" x="212" y="206" font-size="88">RUNDUM-SORGLOS</text>
  <text class="headline" x="212" y="330" font-size="88">WÄSCHEREI</text>

  <!-- Leistungen -->
  <g class="service-list">
    <path class="tick" d="M88 436 l8 10 l14 -22"/>
    <text class="service-item" x="116" y="455" font-size="26">Hotel- und Gastronomiewäsche</text>
    <path class="tick" d="M88 486 l8 10 l14 -22"/>
    <text class="service-item" x="116" y="505" font-size="26">Schmutzmatten</text>
    <path class="tick" d="M88 534 l8 10 l14 -22"/>
    <text class="service-item" x="116" y="553" font-size="26">Gardinenservice</text>

    <path class="tick" d="M632 436 l8 10 l14 -22"/>
    <text class="service-item" x="660" y="455" font-size="26">Berufskleidung</text>
    <path class="tick" d="M632 486 l8 10 l14 -22"/>
    <text class="service-item" x="660" y="505" font-size="26">Private Wäsche</text>
    <path class="tick" d="M632 534 l8 10 l14 -22"/>
    <text class="service-item" font-size="26">
      <tspan x="660" y="553">Verkauf von Hotel- und</tspan>
      <tspan x="662" y="585">Gastronomietextilien</tspan>
    </text>
  </g>

  <!-- Absender -->
  <text class="brand-name" x="36" y="795" font-size="46">Wäscherei Lindenfeld</text>
  <text class="contact" font-size="24">
    <tspan x="702" y="760">Ahornweg 12 – 70999 Musterstadt</tspan>
    <tspan x="702" y="792">Tel. +49 (0) 7000 / 12 34 56</tspan>
    <tspan x="702" y="824">E-Mail. info@lindenfeld.de</tspan>
  </text>
</svg>

</body>
</html>
```